New Business Card Design Project VORALDI-Italy

we are VORALDI-Italy
our company in the market for 3 years we are luxury cosmetic company and its about time for a facelift :)
i will like to have elegant luxurious and unique business card
that will give the person that get it a unique, luxurious and elegant impression
I'm VERY OPEN FOR NEW IDEAS , even duo i add a few files of things that i see on line and i like them

i add my logo as well
my website is VORALDI.COM
(if you would like to see the main style that we have)

Target Market(s)

adult that have money :)

Industry/Entity Type

Business

Contact Information for Business Card

Name - Paul Voraldi
Position - CEO and CO Founder
address - 4718 E Danbury
telephone - 555-318-4402
email - paul@voraldi-example.com
fax - 555-318-4402
website - VORALDI.COM

Colors
000000
959595
fbee3e
ffffff

Requirements
Must have
• big logo in GOLD color
• elegant look
• impressive
Nice to have
• not must but maybe classy pattern background
• not must but maybe emblem
• maybe clear plastic business card
Should not have
• colors
• images

```html
<!DOCTYPE html>
<html lang="en">
<head>
<meta charset="utf-8">
<title>VORALDI Italy – Business Card</title>
<link href="https://fonts.googleapis.com/css2?family=Roboto:wght@400;500;700&family=Tinos&display=swap" rel="stylesheet">
<style>
  :root {
    --backdrop: #202020;
    --card-white: #f4f4f4;
    --gold: #d4ad45;
    --gold-light: #e3c76a;
    --gold-deep: #cfa63d;
    --ink: #3c3c3c;
    --rule: #8a8a8a;
    --band-grey: #6e6e6e;
    --white: #ffffff;
  }
  * { margin: 0; padding: 0; box-sizing: border-box; }
  html, body {
    width: 1200px; height: 960px; overflow: hidden;
    background: var(--backdrop);
  }
  .stage { position: relative; width: 1200px; height: 960px; }

  .card {
    position: absolute; width: 600px; height: 342px;
    border-radius: 18px; overflow: hidden;
  }

  /* Front */
  .card-front { left: 314px; top: 114px; background: var(--card-white); }
  .brand-mark {
    position: absolute; left: 439px; top: 31px;
    width: 80px; height: 80px; border-radius: 50%;
    background: var(--gold);
  }
  .brand-name {
    position: absolute; right: 34px; width: 200px; text-align: center;
    font-family: "Tinos", "Times New Roman", serif; font-weight: 400;
    color: var(--gold);
  }
  .brand-name .word { position: absolute; left: 0; right: 0; top: 125px; font-size: 35px; line-height: 1; }
  .brand-name .country { position: absolute; left: 0; right: 0; top: 175px; font-size: 14px; line-height: 1; }

  .holder { position: absolute; left: 31px; top: 182px; font-family: "Roboto", sans-serif; }
  .holder-name { color: var(--gold); font-size: 23px; font-weight: 700; line-height: 1; }
  .holder-role { color: var(--ink); font-size: 15px; margin-top: 6px; }

  .divider { position: absolute; left: 30px; right: 31px; top: 237px; height: 1px; background: var(--rule); }

  .contact { position: absolute; top: 252px; font-family: "Roboto", sans-serif; font-size: 14px; line-height: 20px; color: var(--ink); }
  .contact-left { left: 29px; }
  .contact-right { right: 30px; text-align: right; }
  .label { color: var(--gold); font-weight: 700; }

  .band-grey { position: absolute; left: 0; bottom: 0; width: 360px; height: 12px; background: var(--band-grey); }
  .band-gold {
    position: absolute; right: 0; bottom: 0; width: 262px; height: 32px;
    background: linear-gradient(90deg, var(--gold-deep), var(--gold-light));
    clip-path: polygon(22px 0, 100% 0, 100% 100%, 0 100%);
  }
  .site-front {
    position: absolute; right: 30px; bottom: 9px;
    font-family: "Roboto", sans-serif; font-size: 14px; color: var(--white); letter-spacing: 0.3px;
  }

  /* Back */
  .card-back {
    left: 311px; top: 473px;
    background: radial-gradient(ellipse at 62% 50%, #e4c96c 0%, var(--gold-deep) 75%);
  }
  .back-mark {
    position: absolute; left: 12px; top: 10px; width: 320px; height: 320px;
    border-radius: 50%; background: rgba(255, 240, 190, 0.12);
  }
  .back-brand {
    position: absolute; right: 48px; width: 196px; text-align: center;
    font-family: "Tinos", "Times New Roman", serif; font-weight: 400; color: var(--white);
  }
  .back-brand .word { position: absolute; left: 0; right: 0; top: 218px; font-size: 38px; line-height: 1; }
  .back-brand .country { position: absolute; left: 0; right: 0; top: 272px; font-size: 15px; line-height: 1; }
  .site-back {
    position: absolute; right: 48px; top: 293px;
    font-family: "Roboto", sans-serif; font-size: 14px; letter-spacing: 3.4px; color: var(--white);
  }
</style>
</head>
<body>
<main class="stage">
  <section class="card card-front" aria-label="Business card front">
    <div class="brand-mark" aria-hidden="true"></div>
    <div class="brand-name" style="top:0;height:200px;">
      <span class="word">VORALDI</span>
      <span class="country">ITALY</span>
    </div>

    <div class="holder">
      <p class="holder-name">PAUL VORALDI</p>
      <p class="holder-role">CEO &amp; CO Founder</p>
    </div>

    <div class="divider"></div>

    <div class="contact contact-left">
      <p><span class="label">Phone:</span> 555-318-4402</p>
      <p><span class="label">Fax:</span> 555-318-4402</p>
    </div>
    <div class="contact contact-right">
      <p>4718 E Danbury</p>
      <p><span class="label">Email:</span> paul@voraldi-example.com</p>
    </div>

    <div class="band-grey"></div>
    <div class="band-gold"></div>
    <p class="site-front">WWW.VORALDI.COM</p>
  </section>

  <section class="card card-back" aria-label="Business card back">
    <div class="back-mark" aria-hidden="true"></div>
    <div class="back-brand" style="top:0;height:300px;">
      <span class="word">VORALDI</span>
      <span class="country">ITALY</span>
    </div>
    <p class="site-back">www.voraldi.com</p>
  </section>
</main>
</body>
</html>
```